Vellorin - Business Cards for a new venture

create business card for a startup classified business dealing in construction materials, the cards need to have a professional look but modern, more serious than playful, one of the samples must include the official font (attached), please explore using the official colors in the company's logo

Target Market(s)

Energy sector

Contact Information for Business Card

Font styles to use
Other font styles liked:
• suissnord

Requirements
Must have
• corporate colors (in logo attached)
Nice to have
• Official font (in one of the samples) font is : suissnord
Should not have
• Cartoonish look

```html
<!DOCTYPE html>
<html lang="en">
<head>
<meta charset="utf-8">
<title>Vellorin – Business Cards</title>
<link rel="stylesheet" href="https://fonts.googleapis.com/css2?family=Roboto:wght@400;500&family=Roboto+Condensed:wght@700&display=swap">
<style>
  :root {
    --backdrop: #2b2b2d;
    --card: #f7f7f6;
    --brand-blue: #1f4e8c;
    --brand-grey: #8e9195;
    --ink: #4f5154;
    --rule: #c9cacc;
  }
  * { box-sizing: border-box; margin: 0; padding: 0; }
  html, body { width: 1200px; height: 900px; overflow: hidden; }
  body {
    background: var(--backdrop);
    font-family: "Roboto", Arial, sans-serif;
    display: flex;
    flex-direction: column;
    align-items: center;
    justify-content: center;
    gap: 44px;
  }
  .card {
    position: relative;
    width: 660px;
    height: 378px;
    background: var(--card);
    box-shadow: 0 6px 18px rgba(0,0,0,.35);
  }
  /* front */
  .card-front {
    display: flex;
    align-items: center;
    justify-content: center;
  }
  .brand-name {
    display: flex;
    align-items: center;
    gap: 16px;
    font-family: "Roboto", Arial, sans-serif;
    font-weight: 400;
    font-size: 40px;
    letter-spacing: 10px;
    text-transform: uppercase;
    color: var(--brand-grey);
  }
  .brand-dot {
    width: 14px; height: 14px;
    border-radius: 50%;
    background: var(--brand-blue);
  }
  /* back */
  .holder {
    position: absolute;
    right: 378px;
    top: 150px;
    text-align: right;
  }
  .holder-name {
    font-family: "Roboto Condensed", Arial, sans-serif;
    font-weight: 700;
    font-size: 27px;
    color: var(--brand-blue);
    line-height: 1;
  }
  .holder-role {
    font-family: "Roboto Condensed", Arial, sans-serif;
    font-weight: 700;
    font-size: 14px;
    letter-spacing: .5px;
    color: var(--brand-grey);
    margin-top: 4px;
  }
  .divider {
    position: absolute;
    left: 300px;
    top: 140px;
    width: 1px;
    height: 108px;
    background: var(--rule);
  }
  .contact-list {
    position: absolute;
    left: 318px;
    top: 146px;
    list-style: none;
  }
  .contact-list li {
    display: flex;
    align-items: center;
    gap: 10px;
    font-size: 16px;
    color: var(--ink);
    height: 24px;
  }
  .icon { width: 14px; height: 14px; fill: var(--brand-blue); flex: none; }
  .address {
    position: absolute;
    left: 32px;
    bottom: 50px;
    display: flex;
    align-items: center;
    gap: 8px;
    font-size: 17px;
    color: var(--ink);
  }
</style>
</head>
<body>

<section class="card card-front" aria-label="Card front">
  <div class="brand-name"><span class="brand-dot"></span>Vellorin</div>
</section>

<section class="card card-back" aria-label="Card back">
  <div class="holder">
    <p class="holder-name">DANIEL HART</p>
    <p class="holder-role">CEO/FOUNDER</p>
  </div>
  <div class="divider"></div>
  <ul class="contact-list">
    <li>
      <svg class="icon" viewBox="0 0 24 24"><path d="M6.6 10.8a15.1 15.1 0 0 0 6.6 6.6l2.2-2.2c.3-.3.7-.4 1-.2 1.1.4 2.3.6 3.6.6.6 0 1 .4 1 1V20c0 .6-.4 1-1 1C10.6 21 3 13.4 3 4c0-.6.4-1 1-1h3.5c.6 0 1 .4 1 1 0 1.3.2 2.5.6 3.6.1.3 0 .7-.2 1z"/></svg>
      604 318 2295
    </li>
    <li>
      <svg class="icon" viewBox="0 0 24 24"><path d="M7 1h10a2 2 0 0 1 2 2v18a2 2 0 0 1-2 2H7a2 2 0 0 1-2-2V3a2 2 0 0 1 2-2zm0 3v14h10V4zm5 15.5a1 1 0 1 0 0 2 1 1 0 0 0 0-2z"/></svg>
      812 557 4073
    </li>
    <li>
      <svg class="icon" viewBox="0 0 24 24"><path d="M2 5h20v14H2zm2 2v.4l8 5.2 8-5.2V7zm0 2.8V17h16V9.8l-8 5.2z"/></svg>
      daniel@vellorin.com
    </li>
    <li>
      <svg class="icon" viewBox="0 0 24 24"><path d="M12 2a10 10 0 1 0 0 20 10 10 0 0 0 0-20zm-1 17.9A8 8 0 0 1 4.1 10L9 15v1a2 2 0 0 0 2 2zm6.9-2.5A2 2 0 0 0 16 16h-1v-3a1 1 0 0 0-1-1H8v-2h2a1 1 0 0 0 1-1V7h2a2 2 0 0 0 2-2v-.4a8 8 0 0 1 2.9 12.8z"/></svg>
      www.vellorin.com
    </li>
  </ul>
  <p class="address">
    <svg class="icon" viewBox="0 0 24 24" style="width:15px;height:17px"><path d="M12 2a7 7 0 0 0-7 7c0 5.2 7 13 7 13s7-7.8 7-13a7 7 0 0 0-7-7zm0 9.5a2.5 2.5 0 1 1 0-5 2.5 2.5 0 0 1 0 5z"/></svg>
    2140 Larkspur Road, Fairbanks, Alaska 34518
  </p>
</section>

</body>
</html>
```